Cybersecurity Course - Bastion Trailplan: HOLV TPX Program

this is a graphic for a course I will launch. I have attached the ebook that will accompany the course. Logo also attached.

Size is 1280 x 720 pixels, with a minimum width of 640 pixels. The aspect ratio should be 16:9. The maximum file size is 2 MB.

Title: Bastion Trailplan: HOLV TPX Program
- MASTER Governance Risk Management & Compliance (GRC) with HOLV TPX 2.0
- Learn through real-world industry applications, examples, and samples
- Access downloadable HOLV TPX 2.0 resources and experience a guided walkthrough with a mentor

Target Market(s)

IT services

Industry/Entity Type

cybersecurity

Colors
0054AA
0677BA
7BADD7
CADEEF
E8F1F8

Requirements
Must have
• 1280 x 720 pixel

```html
<!DOCTYPE html>
<html lang="en">
<head>
<meta charset="utf-8">
<title>Bastion Trailplan: HOLV TPX Program</title>
<link rel="stylesheet" href="https://fonts.googleapis.com/css2?family=Bebas+Neue&family=Montserrat:wght@400;700&display=swap">
<style>
  :root {
    --stage: #e4e4e4;
    --paper: #f2f3f3;
    --paper-glow: #fbfbfb;
    --accent: #00aaff;
    --ink: #0a0a0a;
    --body-ink: #1c1c1c;
    --white: #ffffff;
    --forest-light: #8fb35a;
    --forest-mid: #4f7a32;
    --forest-dark: #2c4f20;
  }
  * { margin: 0; padding: 0; box-sizing: border-box; }
  html, body {
    width: 1199px; height: 1200px; overflow: hidden;
    background: var(--stage);
  }
  .course-graphic {
    position: absolute; left: 0; top: 263px;
    width: 1199px; height: 674px;
    background: radial-gradient(ellipse at 45% 50%, var(--paper-glow) 0%, var(--paper) 75%);
    overflow: hidden;
  }
  .brand {
    position: absolute; left: 48px; top: 34px;
    display: flex; align-items: center; gap: 14px;
  }
  .brand-dot {
    width: 40px; height: 40px; border-radius: 50%;
    border: 3px solid var(--accent);
  }
  .brand-name {
    font-family: "Montserrat", sans-serif; font-weight: 700;
    font-size: 20px; letter-spacing: 2px; color: var(--accent);
  }
  .title {
    position: absolute; left: 46px; top: 100px;
    font-family: "Bebas Neue", sans-serif; font-size: 104px; line-height: 1;
    font-weight: 400; color: var(--ink); letter-spacing: 0.5px; white-space: nowrap;
  }
  .program-band {
    position: absolute; left: 0; top: 212px; width: 710px; height: 70px;
    background: var(--accent);
    display: flex; align-items: center; padding: 6px 0 0 48px;
    font-family: "Bebas Neue", sans-serif; font-size: 70px; line-height: 1;
    color: var(--white); letter-spacing: 1px;
  }
  .benefits {
    position: absolute; left: 48px; top: 318px; list-style: none;
    display: flex; flex-direction: column; gap: 16px;
  }
  .benefit {
    display: flex; align-items: center; gap: 14px;
    font-family: "Montserrat", sans-serif; font-weight: 400;
    font-size: 19px; line-height: 25px; color: var(--body-ink);
  }
  .benefit strong { font-weight: 700; color: var(--ink); }
  .tick-box { width: 21px; height: 21px; flex: none; }
  .course-visual {
    position: absolute; left: 760px; top: 40px; width: 392px; height: 510px;
    border-radius: 24px;
    background: linear-gradient(150deg, var(--forest-light) 0%, var(--forest-mid) 55%, var(--forest-dark) 100%);
  }
  .author-band {
    position: absolute; left: 0; right: 0; bottom: 0; height: 74px;
    background: var(--accent);
    display: flex; align-items: center; justify-content: center; padding-top: 5px;
    font-family: "Bebas Neue", sans-serif; font-size: 58px; line-height: 1;
    color: var(--white);
  }
</style>
</head>
<body>
  <main class="course-graphic">
    <div class="brand">
      <span class="brand-dot"></span>
      <span class="brand-name">KESTRELPATH ACADEMY</span>
    </div>

    <h1 class="title">BASTION TRAILPLAN</h1>

    <div class="program-band">HOLV TPX PROGRAM</div>

    <ul class="benefits">
      <li class="benefit">
        <svg class="tick-box" viewBox="0 0 22 22"><rect width="22" height="22" fill="var(--accent)"/><path d="M5 11.5 L9.5 16 L17.5 4.5" fill="none" stroke="var(--white)" stroke-width="2.6" stroke-linecap="round" stroke-linejoin="round"/></svg>
        <span><strong>MASTER</strong> Governance Risk Management<br>and Compliance (<strong>GRC</strong>) with <strong>HOLV TPX 2.0</strong></span>
      </li>
      <li class="benefit">
        <svg class="tick-box" viewBox="0 0 22 22"><rect width="22" height="22" fill="var(--accent)"/><path d="M5 11.5 L9.5 16 L17.5 4.5" fill="none" stroke="var(--white)" stroke-width="2.6" stroke-linecap="round" stroke-linejoin="round"/></svg>
        <span>Learn Through Real-World Industry<br>Applications, Examples, Samples</span>
      </li>
      <li class="benefit">
        <svg class="tick-box" viewBox="0 0 22 22"><rect width="22" height="22" fill="var(--accent)"/><path d="M5 11.5 L9.5 16 L17.5 4.5" fill="none" stroke="var(--white)" stroke-width="2.6" stroke-linecap="round" stroke-linejoin="round"/></svg>
        <span>Access Downloadable <strong>HOLV TPX 2.0</strong> Resources and<br>Experience a Guided Walkthrough with a Mentor</span>
      </li>
    </ul>

    <div class="course-visual" role="img" aria-label="Shield emblem with circuit lines framing a miniature forest landscape and winding road with map pins"></div>

    <div class="author-band">DANA WHITFIELD, CISSP, CGRC</div>
  </main>
</body>
</html>
```